Brightwell Fellowship Chapel 70th Anniversary

A poster to advertise our 70th Church Anniversary. 1951 - 2021

Brightwell Fellowship Chapel

“We will tell the next generation “ Psalm 78:4

Brightwell Fellowship Chapel, Marlow Lane, Hereford, HR4 9TX

www.brightwellchapel.org.uk

T: 01432 867201
E: office@brightwellchapel.org.uk

We give thanks for all that God has done...

Font styles to use
Serif
Sans Serif
Decorative

Requirements
Nice to have
• A modern design and text
Should not have
• Crosses or pictures of churches, doves etc...

```html
<!DOCTYPE html>
<html lang="en">
<head>
<meta charset="utf-8">
<title>Brightwell Fellowship Chapel – 70th Anniversary Poster</title>
<link href="https://fonts.googleapis.com/css2?family=Montserrat:wght@300;400;500;700;800;900&family=Allura&display=swap" rel="stylesheet">
<style>
  :root {
    --board: #231f20;
    --paper: #ededed;
    --ink: #0b0b0b;
    --violet: #6a1fd6;
    --blue: #3d5ef0;
    --royal: #3a4fe0;
    --contact: #2f4fc4;
    --crowd: #d2d2d2;
  }
  * { margin: 0; padding: 0; box-sizing: border-box; }
  html, body { width: 1200px; height: 700px; overflow: hidden; background: var(--board); }
  body { position: relative; font-family: "Montserrat", sans-serif; }

  .poster {
    position: absolute; top: 100px; width: 500px; height: 500px;
    background: var(--paper); overflow: hidden;
  }
  .poster--standard { left: 84px; }
  .poster--anniversary { left: 632px; }

  .crowd-backdrop {
    position: absolute; left: 0; right: 0; top: 290px; bottom: 0;
    background: linear-gradient(180deg, rgba(210,210,210,0) 0%, var(--crowd) 35%, #dcdcdc 100%);
  }

  .anniversary-line {
    position: absolute; top: 17px; left: 0; right: 0; text-align: center;
    font-weight: 800; font-size: 11.5px; color: var(--royal); letter-spacing: -0.2px;
  }

  .brand {
    position: absolute; left: 0; right: 0; top: 40px;
    display: flex; flex-direction: column; align-items: center;
  }
  .poster--anniversary .brand { top: 50px; }
  .brand__dot { width: 72px; height: 72px; border-radius: 50%; background: var(--ink); }
  .brand__name {
    margin-top: 14px; text-align: center; color: var(--ink);
    font-weight: 500; font-size: 24px; line-height: 1.1; letter-spacing: 1px; text-transform: uppercase;
  }

  .headline {
    position: absolute; left: 0; right: 0; top: 213px; text-align: center;
    text-transform: uppercase; font-weight: 900; line-height: 1;
  }
  .headline span {
    display: block;
    background: linear-gradient(90deg, var(--blue), var(--violet));
    -webkit-background-clip: text; background-clip: text; color: transparent;
  }
  .headline__lead { font-size: 30px; letter-spacing: -0.5px; }
  .headline__key { font-size: 57px; letter-spacing: -1px; margin-top: 2px; }

  .verse-tag {
    position: absolute; left: 312px; top: 292px; width: 168px; height: 40px;
    transform: rotate(-7deg);
    background: linear-gradient(90deg, var(--blue), var(--violet));
    box-shadow: 2px 2px 0 #fff;
    color: #fff; display: flex; align-items: center; justify-content: center; gap: 8px;
  }
  .verse-tag__book { font-family: "Allura", cursive; font-size: 30px; }
  .verse-tag__ref { font-weight: 300; font-size: 22px; }

  .address {
    position: absolute; left: 40px; right: 40px; top: 352px; text-align: center;
    color: var(--ink); font-weight: 700; font-size: 24px; line-height: 1.15; letter-spacing: -0.4px;
  }
  .thanks-band {
    position: absolute; left: 40px; width: 423px; top: 420px; height: 21px;
    background: linear-gradient(180deg, var(--violet), var(--blue));
    color: #fff; font-weight: 700; font-size: 16px; line-height: 21px; text-align: center;
  }
  .contacts {
    position: absolute; left: 40px; right: 37px; top: 458px;
    display: flex; justify-content: space-between; align-items: center;
    color: var(--contact); font-size: 9.5px; font-weight: 500;
  }
  .contacts li { list-style: none; display: flex; align-items: center; gap: 5px; }
  .contacts svg { width: 10px; height: 10px; }
</style>
</head>
<body>

<!-- Variant without anniversary line -->
<section class="poster poster--standard">
  <div class="crowd-backdrop" role="img" aria-label="Faint photo of a crowd with raised hands in worship"></div>
  <div class="brand">
    <div class="brand__dot"></div>
    <div class="brand__name">Brightwell Fellowship<br>Chapel</div>
  </div>
  <h1 class="headline">
    <span class="headline__lead">“We will tell the next</span>
    <span class="headline__key">Generation”</span>
  </h1>
  <div class="verse-tag"><span class="verse-tag__book">Psalm</span><span class="verse-tag__ref">78:4</span></div>
  <p class="address">Brightwell Fellowship Chapel,<br>Marlow Lane, Hereford, HR4 9TX</p>
  <p class="thanks-band">We give thanks for all that God has done...</p>
  <ul class="contacts">
    <li><svg viewBox="0 0 10 10"><circle cx="5" cy="5" r="5" fill="currentColor"/><path d="M3.2 2.6l1 1-.5.7c.4.8 1 1.4 1.8 1.8l.7-.5 1 1-.6.8C4.8 7.3 2.8 5.3 2.6 3.2z" fill="#fff"/></svg>01432 867201</li>
    <li><svg viewBox="0 0 10 10"><circle cx="5" cy="5" r="5" fill="currentColor"/><path d="M3 7l4-4M3.5 5L2.8 5.7a1 1 0 001.5 1.5L5 6.5M6.5 5l.7-.7a1 1 0 00-1.5-1.5L5 3.5" stroke="#fff" stroke-width=".8" fill="none"/></svg>office@brightwellchapel.org.uk</li>
    <li><svg viewBox="0 0 10 10"><circle cx="5" cy="5" r="5" fill="currentColor"/><path d="M3 7l4-4M3.5 5L2.8 5.7a1 1 0 001.5 1.5L5 6.5M6.5 5l.7-.7a1 1 0 00-1.5-1.5L5 3.5" stroke="#fff" stroke-width=".8" fill="none"/></svg>www.brightwellchapel.org.uk</li>
  </ul>
</section>

<!-- Variant with anniversary line -->
<section class="poster poster--anniversary">
  <div class="crowd-backdrop" role="img" aria-label="Faint photo of a crowd with raised hands in worship"></div>
  <p class="anniversary-line">70TH CHURCH ANNIVERSARY. 1951 - 2021</p>
  <div class="brand">
    <div class="brand__dot"></div>
    <div class="brand__name">Brightwell Fellowship<br>Chapel</div>
  </div>
  <h1 class="headline">
    <span class="headline__lead">“We will tell the next</span>
    <span class="headline__key">Generation”</span>
  </h1>
  <div class="verse-tag"><span class="verse-tag__book">Psalm</span><span class="verse-tag__ref">78:4</span></div>
  <p class="address">Brightwell Fellowship Chapel,<br>Marlow Lane, Hereford, HR4 9TX</p>
  <p class="thanks-band">We give thanks for all that God has done...</p>
  <ul class="contacts">
    <li><svg viewBox="0 0 10 10"><circle cx="5" cy="5" r="5" fill="currentColor"/><path d="M3.2 2.6l1 1-.5.7c.4.8 1 1.4 1.8 1.8l.7-.5 1 1-.6.8C4.8 7.3 2.8 5.3 2.6 3.2z" fill="#fff"/></svg>01432 867201</li>
    <li><svg viewBox="0 0 10 10"><circle cx="5" cy="5" r="5" fill="currentColor"/><path d="M3 7l4-4M3.5 5L2.8 5.7a1 1 0 001.5 1.5L5 6.5M6.5 5l.7-.7a1 1 0 00-1.5-1.5L5 3.5" stroke="#fff" stroke-width=".8" fill="none"/></svg>office@brightwellchapel.org.uk</li>
    <li><svg viewBox="0 0 10 10"><circle cx="5" cy="5" r="5" fill="currentColor"/><path d="M3 7l4-4M3.5 5L2.8 5.7a1 1 0 001.5 1.5L5 6.5M6.5 5l.7-.7a1 1 0 00-1.5-1.5L5 3.5" stroke="#fff" stroke-width=".8" fill="none"/></svg>www.brightwellchapel.org.uk</li>
  </ul>
</section>

</body>
</html>
```